South Carolina Bridal and Formal Wear Store

We want The Gown Parlor of Ashcombe website to feel luxurious, elegant, welcoming, and approachable—without feeling overpriced or intimidating. The site should immediately show that we are a full-service bridal and formal wear destination, offering bridal gowns, prom, mothers’ dresses, tuxedos and suits, accessories, and more. We want beautiful, high-end imagery and a clean, modern design while still reflecting the warm, personal experience customers receive when they walk into our boutique. Most importantly, the website should be easy to shop and navigate, allowing customers to browse our collections, see what we offer, understand price ranges, book appointments, and feel excited and comfortable choosing The Gown Parlor of Ashcombe for all of their special-event needs.

Target Market(s)

Women ages 18-50. Brides, engaged women, mothers of the occasion

Industry/Entity Type

Bridal and Formal Wear

Coding

Coded - Design and coding required

Number of Pages Required

5+ page

Font styles to use
Sans Serif

Colors

Designer to choose colors to be used in the design.

Requirements
Must have
• Appointment area, about us staff area, what we offer and designers our logo
Nice to have
• Modern Southern Luxury: Clean, elegant, and upscale with soft neutral tones, beautiful bridal photography, and a warm Lowcountry feel.
Should not have
• pricing

```html
<!DOCTYPE html>
<html lang="en">
<head>
<meta charset="utf-8">
<title>The Gown Parlor of Ashcombe</title>
<link href="https://fonts.googleapis.com/css2?family=Marcellus&family=Jost:wght@400;500&display=swap" rel="stylesheet">
<style>
:root{
  --accent:#c48a62;
  --ink:#1e1a17;
  --text:#4a4340;
  --cream:#f6f0ea;
  --tan:#efe3d8;
  --white:#ffffff;
  --gold:#d9a25e;
  --soft:#ecdccf;
}
*{box-sizing:border-box;margin:0;padding:0}
html,body{width:1200px;height:4926px;overflow:hidden}
body{position:relative;background:var(--white);font-family:'Jost',sans-serif;color:var(--text)}
.abs{position:absolute}
.serif{font-family:'Marcellus',serif;font-weight:400}
.btn{position:absolute;display:flex;align-items:center;justify-content:center;background:var(--accent);color:var(--white);font:500 15px 'Jost',sans-serif;letter-spacing:.5px;text-transform:uppercase;outline:2px solid var(--accent);outline-offset:3px}
.site-header{position:absolute;top:0;left:0;width:1200px;height:84px;background:var(--white)}
.brand{position:absolute;font:500 15px/18px 'Jost',sans-serif;color:var(--ink);letter-spacing:.5px}
.nav a{position:absolute;top:32px;font:500 14px 'Jost',sans-serif;color:var(--ink);text-decoration:none;letter-spacing:.3px}
.nav a.active::after{content:"";position:absolute;left:50%;margin-left:-10px;top:24px;width:20px;height:2px;background:var(--accent)}
.divider{position:absolute;left:900px;top:20px;width:1px;height:44px;background:#ddd}
.icon-circle{position:absolute;border-radius:50%;background:var(--accent);display:flex;align-items:center;justify-content:center}
.hero{position:absolute;top:84px;left:0;width:1200px;height:633px;overflow:hidden}
.hero-photo{position:absolute;inset:0;background:linear-gradient(90deg,#b59366 0%,#cdb08a 30%,#dcc6a8 46%,#c9a993 56%,#5b4a42 70%,#2f2a27 84%,#3e3631 100%)}
.hero h1{position:absolute;left:86px;top:94px;font-size:57px;line-height:54px;color:var(--white);letter-spacing:1px}
.hero p{position:absolute;left:86px;top:284px;width:400px;font-size:15px;line-height:24px;color:var(--white)}
.section-title{position:absolute;font-size:52px;line-height:56px;color:var(--ink);letter-spacing:1px}
.section-title .light{color:var(--accent)}
.body-copy{position:absolute;font-size:15px;line-height:24px;color:var(--text)}
.rule{position:absolute;height:2px;background:var(--accent)}
.offer{position:absolute;top:1391px;left:0;width:1200px;height:803px;background:var(--cream)}
.center{text-align:center;left:0;width:1200px}
.offer-card{position:absolute;top:239px;width:252px;height:392px;background:var(--tan)}
.offer-card .photo{height:329px}
.offer-card span{display:block;text-align:center;padding-top:19px;font:500 19px 'Jost',sans-serif;color:var(--ink)}
.feature{position:absolute;left:84px}
.feature h3{position:absolute;left:84px;top:-20px;font:500 19px 'Jost',sans-serif;color:var(--ink);white-space:nowrap}
.feature p{position:absolute;left:84px;top:8px;font-size:15px;color:var(--text);white-space:nowrap}
.staff{position:absolute;top:2872px;left:0;width:1200px;height:673px;background:var(--accent)}
.staff-card{position:absolute;top:243px;width:195px;height:350px}
.staff-card .photo{height:285px;background:linear-gradient(180deg,#8d8681 0%,#5a524e 22%,#3a3330 48%,#1d1a19 100%)}
.staff-card .tag{position:absolute;left:11px;top:273px;width:173px;height:77px;background:var(--white);text-align:center;padding-top:14px}
.staff-card .tag::before{content:"";position:absolute;left:0;top:0;border-top:14px solid var(--accent);border-right:14px solid transparent}
.staff-card b{display:block;font:500 19px 'Jost',sans-serif;color:var(--ink)}
.staff-card small{display:block;font-size:15px;color:var(--text)}
.form-panel{position:absolute;left:604px;top:3786px;width:510px;height:466px;background:var(--cream);border:1px solid #eadccf}
.field{position:absolute;left:29px;width:450px;height:48px;background:var(--white);font-size:15px;color:#555;padding:14px 20px}
.field svg{position:absolute;right:18px;top:16px}
.footer{position:absolute;top:4440px;left:0;width:1200px;height:486px;background:var(--cream)}
.footer h4{position:absolute;font:500 18px 'Jost',sans-serif;color:var(--ink)}
.footer a{position:absolute;font-size:14px;color:var(--ink);text-decoration:none}
.social{position:absolute;width:40px;height:40px;border-radius:50%;background:var(--soft)}
.social.on{background:var(--gold)}
.copyright{position:absolute;left:0;width:1200px;top:4872px;text-align:center;font-size:14px;color:var(--ink)}
</style>
</head>
<body>

<header class="site-header">
  <div class="brand" style="left:84px;top:24px">The Gown Parlor<br>of Ashcombe</div>
  <nav class="nav">
    <a href="#" class="active" style="left:405px">HOME</a>
    <a href="#" style="left:495px">ABOUT US</a>
    <a href="#" style="left:613px">OUR STAFF</a>
    <a href="#" style="left:738px">WHAT WE OFFER</a>
  </nav>
  <div class="divider"></div>
  <div class="icon-circle" style="left:933px;top:22px;width:38px;height:38px">
    <svg width="18" height="18" viewBox="0 0 24 24"><path fill="#fff" d="M6.6 10.8a15 15 0 006.6 6.6l2.2-2.2a1 1 0 011-.25 11.4 11.4 0 003.6.57 1 1 0 011 1V20a1 1 0 01-1 1A17 17 0 013 4a1 1 0 011-1h3.5a1 1 0 011 1c0 1.25.2 2.45.57 3.57a1 1 0 01-.25 1z"/></svg>
  </div>
  <div class="abs" style="left:981px;top:24px;font-size:13px;color:var(--ink)">Call Us Anytime:</div>
  <div class="abs" style="left:981px;top:38px;font:500 18px 'Jost',sans-serif;color:var(--ink)">(555) 014-2290</div>
</header>

<section class="hero">
  <div class="hero-photo" role="img" aria-label="Bride embracing groom in a golden field"></div>
  <h1 class="serif">MAKING<br>MEMORY THAT<br>LAST FOREVER</h1>
  <p>Lorem ipsum dolor sit amet consectetur adipiscing elit sed do eiusmod sei tempor incididunt ut labore et dolore magna aliqua quis ipsum suspendi ultrices gravida risus commodo viverra maecenas.</p>
  <div class="btn" style="left:90px;top:415px;width:181px;height:40px">Get Started</div>
  <svg class="abs" style="left:0;top:555px" width="1200" height="78" viewBox="0 0 1200 78">
    <path d="M0 78V40Q600 120 1200 0V78Z" fill="#fff"/>
    <path d="M0 40Q600 126 1200 2Q600 108 0 40Z" fill="var(--accent)"/>
  </svg>
</section>

<section class="about">
  <svg class="abs" style="left:82px;top:822px" width="480" height="470" viewBox="0 0 480 470">
    <circle cx="243" cy="235" r="227" fill="none" stroke="var(--accent)" stroke-width="1.5"/>
    <circle cx="243" cy="235" r="212" fill="none" stroke="var(--accent)" stroke-width="1"/>
    <path d="M40 90Q10 230 80 340Q140 430 210 460" fill="none" stroke="var(--accent)" stroke-width="1.5"/>
  </svg>
  <div class="abs" role="img" aria-label="Boutique team posing together in black dresses in front of gown racks" style="left:120px;top:850px;width:410px;height:410px;border-radius:50%;background:linear-gradient(180deg,#a39a92 0%,#6e625b 30%,#2c2624 60%,#3a302c 100%)"></div>
  <h2 class="section-title serif" style="left:608px;top:798px"><span class="light">LET’S MAKE A</span><br>PLAN TOGETHER</h2>
  <div class="rule" style="left:608px;top:911px;width:242px"></div>
  <p class="body-copy" style="left:608px;top:938px;width:500px">Lorem ipsum dolor sit amet consectetur adipisicing elit se eiusmod tempor incididunt ut labore et dolore magna aliqua ad minim veniam quis nostrud exercitation ullamco laboris nisi ut aliquip commodo is consequat. Duis aute irure dolor in reprehenderit in voluptate velit esse cillum dolore eu fugiat nulla pariatur. Excepteur sint occaecat cupidatat non proident sunt in culpa qui officia deserunt</p>
  <p class="body-copy" style="left:608px;top:1106px;width:500px">Sed ut perspiciatis unde omnis iste natus accusantium laudantium totam rem aperiam, eaque ipsa quae ab illo inventore verita beatae vitae dicta sunt explicabo. Nemo enim ipsam voluptatem quia voluptas aspernatur aut odit aut fugsed quia conse</p>
  <div class="btn" style="left:612px;top:1238px;width:212px;height:44px">More About Us</div>
</section>

<section class="offer">
  <h2 class="section-title serif center" style="top:74px"><span class="light">WHAT WE</span> OFFER</h2>
  <p class="body-copy center" style="top:145px">Lorem ipsum dolor sit amet consectetur adipisicing elit se eiusmod tempor incididunt<br>labore et dolore magna aliqua ad minim veniam quis nostrud exercitation</p>
  <div class="offer-card" style="left:84px"><div class="photo" role="img" aria-label="Strapless ivory bridal ball gown in an ornate room" style="background:linear-gradient(180deg,#9c7e5c 0%,#b89b78 40%,#e3d8c8 70%,#f0ebe3 100%)"></div><span>BRIDAL GOWNS</span></div>
  <div class="offer-card" style="left:343px"><div class="photo" role="img" aria-label="Model in a white corset prom gown" style="background:linear-gradient(180deg,#4f3e31 0%,#7a6552 40%,#d9cfc3 72%,#efe9e2 100%)"></div><span>PROM</span></div>
  <div class="offer-card" style="left:602px"><div class="photo" role="img" aria-label="Woman in a white gown holding flowers in a park" style="background:linear-gradient(180deg,#6e7a58 0%,#8f9a7a 35%,#e9e6e1 70%,#f6f4f1 100%)"></div><span>MOTHERS’ DRESSES</span></div>
  <div class="offer-card" style="left:861px"><div class="photo" role="img" aria-label="Woman in a dark tailored jacket" style="background:linear-gradient(180deg,#a9a8a3 0%,#7d7c78 35%,#2a2c31 65%,#1b1d21 100%)"></div><span>TUXEDOS AND SUITS</span></div>
  <div class="btn" style="left:513px;top:672px;width:174px;height:42px">View More</div>
</section>

<section class="why">
  <h2 class="section-title serif" style="left:86px;top:2265px"><span class="light">WHY YOU CAN</span><br>CHOOSE US</h2>
  <div class="rule" style="left:86px;top:2378px;width:350px"></div>
  <p class="body-copy" style="left:86px;top:2409px;width:490px">Lorem ipsum dolor sit amet consectetur adipisicing elit se eiusmod tempor incididunt ut labore et dolore magna aliqua ad minim venia quis nostrud exercitation ullamco laboris nisi ut aliquip</p>
  <div class="feature" style="top:2534px">
    <div class="icon-circle" style="left:0;top:-33px;width:66px;height:66px"><svg width="28" height="28" viewBox="0 0 24 24"><path fill="#fff" d="M9 3h6l-2 4h-2zM6 20c0-6 3-11 6-11s6 5 6 11z"/></svg></div>
    <h3>BUDGET FRIENDLY</h3><p>Onsectetur adipisicing elit se eius dolore</p>
  </div>
  <div class="feature" style="top:2616px">
    <div class="icon-circle" style="left:0;top:-33px;width:66px;height:66px;background:var(--gold)"><svg width="28" height="28" viewBox="0 0 24 24"><circle cx="12" cy="6" r="3" fill="#fff"/><path fill="#fff" d="M7 20l2-9h6l2 9z"/></svg></div>
    <h3>EXTREME CUSTOMIZATION</h3><p>Dolore magna aliqua ad mini sed</p>
  </div>
  <div class="feature" style="top:2700px">
    <div class="icon-circle" style="left:0;top:-33px;width:66px;height:66px;background:#d9935f"><svg width="30" height="28" viewBox="0 0 30 24"><circle cx="8" cy="8" r="3" fill="#fff"/><circle cx="15" cy="7" r="3.5" fill="#fff"/><circle cx="22" cy="8" r="3" fill="#fff"/><path fill="#fff" d="M3 20c0-5 3-8 5-8s5 3 5 8zM17 20c0-5 3-8 5-8s5 3 5 8zM9 21c0-6 3-9 6-9s6 3 6 9z"/></svg></div>
    <h3>HELPFUL TEAM MEMBER</h3><p>Nostrud exercitation ullamco laboris conse</p>
  </div>
  <svg class="abs" style="left:615px;top:2268px" width="500" height="520" viewBox="0 0 500 520">
    <path d="M445 2H497V70" fill="none" stroke="var(--accent)" stroke-width="2"/>
    <path d="M3 450V517H55" fill="none" stroke="var(--accent)" stroke-width="2"/>
  </svg>
  <div class="abs" role="img" aria-label="Couple kissing at an outdoor wedding, bride in a blush tulle gown" style="left:646px;top:2293px;width:443px;height:470px;background:linear-gradient(180deg,#7d8466 0%,#a39c86 25%,#6b5a4e 45%,#e6c3ae 65%,#f1d6c6 85%,#ddd5cc 100%)"></div>
</section>

<section class="staff">
  <h2 class="section-title serif center" style="top:77px;color:var(--white)">OUR BEAUTIFUL STAFF</h2>
  <p class="body-copy center" style="top:153px;color:var(--white)">Lorem ipsum dolor sit amet consectetur adipisicing elit se eiusmod tempor incididunt<br>labore et dolore magna aliqua ad minim veniam quis nostrud exercitation</p>
  <div class="staff-card" style="left:84px"><div class="photo" role="img" aria-label="Portrait of staff member AD"></div><div class="tag"><b>AD</b><small>Nostrudesrt</small></div></div>
  <div class="staff-card" style="left:293px"><div class="photo" role="img" aria-label="Portrait of staff member CH"></div><div class="tag"><b>CH</b><small>Nostrudesrt</small></div></div>
  <div class="staff-card" style="left:502px"><div class="photo" role="img" aria-label="Portrait of staff member EO"></div><div class="tag"><b>EO</b><small>Nostrudesrt</small></div></div>
  <div class="staff-card" style="left:711px"><div class="photo" role="img" aria-label="Portrait of staff member JB"></div><div class="tag"><b>JB</b><small>Nostrudesrt</small></div></div>
  <div class="staff-card" style="left:920px"><div class="photo" role="img" aria-label="Portrait of staff member NW"></div><div class="tag"><b>NW</b><small>Nostrudesrt</small></div></div>
</section>

<section class="appointment">
  <h2 class="section-title serif center" style="top:3620px"><span class="light">MAKE AN</span> APPOINTMENT</h2>
  <p class="body-copy center" style="top:3697px">Lorem ipsum dolor sit amet consectetur adipisicing elit se eiusmod tempor incididunt<br>labore et dolore magna aliqua ad minim veniam quis nostrud exercitation</p>
  <div class="abs" role="img" aria-label="Bride in a lace gown on a rocky coastline at dusk" style="left:84px;top:3786px;width:510px;height:466px;background:linear-gradient(180deg,#b3b2ae 0%,#c7a283 25%,#8a6e58 45%,#6f6257 62%,#d7cdc3 82%,#f3f0ec 100%)"></div>
  <form class="form-panel">
    <div class="field" style="top:33px">First Name<svg width="16" height="16" viewBox="0 0 24 24"><circle cx="12" cy="7" r="5" fill="#333"/><path fill="#333" d="M3 23c0-6 4-9 9-9s9 3 9 9z"/></svg></div>
    <div class="field" style="top:94px">Last Name<svg width="16" height="16" viewBox="0 0 24 24"><circle cx="12" cy="7" r="5" fill="#333"/><path fill="#333" d="M3 23c0-6 4-9 9-9s9 3 9 9z"/></svg></div>
    <div class="field" style="top:155px">Email Address<svg width="16" height="16" viewBox="0 0 24 24"><path fill="#333" d="M2 5h20v14H2z"/><path d="M3 6l9 7 9-7" fill="none" stroke="#fff" stroke-width="1.5"/></svg></div>
    <div class="field" style="top:216px;height:148px">Write a message for us....<svg width="16" height="16" viewBox="0 0 24 24"><path fill="#333" d="M12 3c5.5 0 10 3.6 10 8s-4.5 8-10 8c-1 0-2-.1-3-.4L4 21l1.3-4A7.6 7.6 0 012 11c0-4.4 4.5-8 10-8z"/></svg></div>
    <div class="btn" style="left:31px;top:381px;width:176px;height:44px">Submit</div>
  </form>
</section>

<svg class="abs" style="left:0;top:4390px" width="1200" height="60" viewBox="0 0 1200 60">
  <path d="M0 60V52Q600 -40 1200 52V60Z" fill="var(--cream)"/>
  <path d="M0 50Q600 -46 1200 50Q600 -28 0 50Z" fill="var(--accent)"/>
</svg>
<footer class="footer">
  <div class="brand" style="left:84px;top:98px">The Gown Parlor<br>of Ashcombe</div>
  <div class="social" style="left:85px;top:161px"></div>
  <div class="social on" style="left:137px;top:161px"></div>
  <div class="social" style="left:186px;top:161px"></div>
  <div class="social" style="left:238px;top:161px"></div>

  <h4 style="left:384px;top:86px">QUICK LINKS</h4>
  <a href="#" style="left:384px;top:135px">Home</a>
  <a href="#" style="left:384px;top:170px">About us</a>
  <a href="#" style="left:384px;top:204px">Our Staff</a>
  <a href="#" style="left:384px;top:237px">What We Offer</a>

  <h4 style="left:630px;top:86px">OTHER LINKS</h4>
  <a href="#" style="left:630px;top:135px">Terms &amp; Condition</a>
  <a href="#" style="left:630px;top:170px">Privacy policy</a>
  <a href="#" style="left:630px;top:204px">FAQs</a>
  <a href="#" style="left:630px;top:237px">Sitemap</a>

  <h4 style="left:877px;top:86px">CONTACT INFO</h4>
  <div class="icon-circle" style="left:877px;top:141px;width:40px;height:40px"><svg width="16" height="18" viewBox="0 0 24 24"><path fill="#fff" d="M12 2a7 7 0 017 7c0 5-7 13-7 13S5 14 5 9a7 7 0 017-7zm0 4.5a2.5 2.5 0 100 5 2.5 2.5 0 000-5z"/></svg></div>
  <div class="abs" style="left:930px;top:135px;font-size:14px;line-height:24px;color:var(--ink)">14 Magnolia Row, Ashcombe,<br>SC 29901</div>
  <div class="icon-circle" style="left:877px;top:191px;width:40px;height:40px"><svg width="16" height="16" viewBox="0 0 24 24"><path fill="#fff" d="M6.6 10.8a15 15 0 006.6 6.6l2.2-2.2a1 1 0 011-.25 11.4 11.4 0 003.6.57 1 1 0 011 1V20a1 1 0 01-1 1A17 17 0 013 4a1 1 0 011-1h3.5a1 1 0 011 1c0 1.25.2 2.45.57 3.57a1 1 0 01-.25 1z"/></svg></div>
  <div class="abs" style="left:930px;top:201px;font-size:14px;color:var(--ink)">(555) 014-2290</div>
  <div class="icon-circle" style="left:877px;top:243px;width:40px;height:40px"><svg width="16" height="14" viewBox="0 0 24 20"><path fill="#fff" d="M1 2h22v16H1z"/><path d="M2 3l10 8 10-8" fill="none" stroke="var(--accent)" stroke-width="2"/></svg></div>
  <div class="abs" style="left:930px;top:253px;font-size:14px;color:var(--ink)">gownparlorhelp.com</div>

  <div class="abs" style="left:0;top:410px;width:1200px;height:1px;background:#e3d6ca"></div>
</footer>
<div class="copyright">Copyright © 2026 Gown Parlor. All rights reserved.</div>

</body>
</html>
```